stationery
business cards, letterhead, and envelopes
Professional
Marisol Dunkerly
Mortgage Loan Originator / Owner
418 Kettering Avenue Ste 2270
Honolulu HI 96813
TideRiverCredit@quillmail.com
www.BrightCedarLending.com
Lowest Rates In Hawaii !!!!!

```html
<!DOCTYPE html>
<html lang="en">
<head>
<meta charset="utf-8">
<title>Bright Cedar Lending – Stationery</title>
<link href="https://fonts.googleapis.com/css2?family=Montserrat:wght@400;600;700&display=swap" rel="stylesheet">
<style>
  :root{
    --board:#e6d5b8;
    --board-dark:#d9c5a3;
    --paper:#ffffff;
    --brand-blue:#2b5fa8;
    --brand-deep:#1f3f8a;
    --sun:#f3c65a;
    --ink:#6b6b6b;
    --label:#7a6a52;
    --grey-flap:#8a8d92;
    --rule:#cfd6e4;
  }
  *{margin:0;padding:0;box-sizing:border-box}
  html,body{width:1200px;height:446px;overflow:hidden}
  body{background:linear-gradient(90deg,var(--board),var(--board-dark) 50%,var(--board));font-family:"Montserrat",sans-serif;position:relative}
  .piece{position:absolute;background:var(--paper);box-shadow:0 2px 5px rgba(0,0,0,.18)}
  .label{position:absolute;font-size:6px;letter-spacing:.12em;text-transform:uppercase;color:var(--label);text-align:center}
  .brand{display:flex;align-items:center;gap:4px;color:var(--brand-blue);font-weight:700;white-space:nowrap}
  .brand .dot{border-radius:50%;background:var(--sun);flex:none}
  .small{font-size:4px;color:var(--ink);line-height:1.5}
  .glow{position:absolute;border-radius:50%;background:radial-gradient(circle,rgba(243,198,90,.28),rgba(43,95,168,.08) 70%,transparent 72%)}

  /* business cards */
  .card{width:100px;height:50px}
  .card-front{left:12px;top:150px;padding:6px 7px}
  .card-front .brand{font-size:6px}
  .card-front .brand .dot{width:8px;height:8px}
  .card-back{left:12px;top:220px;overflow:hidden}
  .card-back .band{height:22px;background:var(--brand-deep)}
  .card-back .brand{font-size:6px;justify-content:center;margin-top:8px}
  .card-back .brand .dot{width:7px;height:7px}
  .card-alt{left:12px;top:292px;display:flex;align-items:center;justify-content:center}
  .card-alt .brand{font-size:6px}
  .card-alt .brand .dot{width:8px;height:8px}

  /* letterheads */
  .letterhead{top:12px;width:300px;height:408px;overflow:hidden}
  .lh-one{left:144px}
  .lh-two{left:473px}
  .lh-one .brand{position:absolute;left:22px;top:16px;font-size:11px}
  .lh-one .brand .dot{width:14px;height:14px}
  .lh-one .contact{position:absolute;left:150px;top:16px;border-left:1px solid var(--rule);padding-left:6px}
  .lh-two .brand{position:absolute;left:0;right:0;top:18px;justify-content:center;font-size:11px}
  .lh-two .brand .dot{width:14px;height:14px}
  .lh-two .footer{position:absolute;left:0;right:0;bottom:14px;text-align:center;font-size:4px;color:var(--ink)}
  .letterhead .glow{left:90px;top:170px;width:130px;height:130px}

  /* envelopes */
  .env-back{left:830px;width:358px;height:88px;overflow:hidden;background:var(--paper)}
  .env-back svg{position:absolute;inset:0}
  .env-blue{top:12px}
  .env-grey{top:104px}
  .env-white{top:196px;display:flex;justify-content:center;padding-top:22px}
  .env-white .dot{width:22px;height:22px;border-radius:50%;background:var(--sun);border:3px solid var(--brand-blue)}
  .env-front{left:820px;top:300px;width:368px;height:120px;overflow:hidden}
  .env-front .brand{position:absolute;left:14px;top:12px;font-size:12px}
  .env-front .brand .dot{width:14px;height:14px}
  .env-front .tag{position:absolute;left:32px;top:30px;font-size:4.5px;color:var(--ink)}
  .env-front .glow{left:270px;top:30px;width:90px;height:90px}
</style>
</head>
<body>

<div class="label" style="left:8px;top:140px;width:108px">Stationery Concepts</div>

<div class="piece card card-front">
  <div class="brand"><span class="dot"></span>Bright Cedar Lending</div>
  <div class="small" style="margin-top:5px">Marisol Dunkerly<br>Mortgage Loan Originator / Owner<br>(808) 555-0142</div>
</div>
<div class="label" style="left:8px;top:206px;width:108px">Business Card Front</div>

<div class="piece card card-back">
  <div class="band"></div>
  <div class="brand"><span class="dot"></span>Bright Cedar Lending</div>
</div>
<div class="label" style="left:8px;top:276px;width:108px">Business Card Front</div>

<div class="piece card card-alt">
  <div class="brand"><span class="dot"></span>Bright Cedar Lending</div>
</div>
<div class="label" style="left:8px;top:348px;width:108px">Business Card Back</div>

<div class="piece letterhead lh-one">
  <div class="brand"><span class="dot"></span>Bright Cedar Lending</div>
  <div class="contact small">418 Kettering Avenue Ste 2270<br>Honolulu HI 96813<br>(808) 555-0142<br>TideRiverCredit@quillmail.com<br>www.BrightCedarLending.com</div>
  <div class="glow" role="img" aria-label="Faint sun and palm background decoration"></div>
</div>
<div class="label" style="left:144px;top:426px;width:300px">Letterhead Option 1</div>

<div class="piece letterhead lh-two">
  <div class="brand"><span class="dot"></span>Bright Cedar Lending</div>
  <div class="glow" role="img" aria-label="Faint sun and palm background decoration"></div>
  <div class="footer">(808) 555-0142 &nbsp;|&nbsp; TideRiverCredit@quillmail.com &nbsp;|&nbsp; www.BrightCedarLending.com</div>
</div>
<div class="label" style="left:473px;top:426px;width:300px">Letterhead Option 2</div>

<div class="piece env-back env-blue">
  <svg width="358" height="88" viewBox="0 0 358 88"><path d="M0 0H358V40Q179 70 0 40Z" fill="var(--brand-deep)"/></svg>
</div>
<div class="piece env-back env-grey">
  <svg width="358" height="88" viewBox="0 0 358 88"><path d="M0 0H358V40Q179 70 0 40Z" fill="var(--grey-flap)"/></svg>
</div>
<div class="piece env-back env-white">
  <svg width="358" height="88" viewBox="0 0 358 88"><path d="M0 0H358V40Q179 70 0 40" fill="none" stroke="var(--rule)"/></svg>
  <span class="dot" style="position:relative"></span>
</div>

<div class="piece env-front">
  <div class="brand"><span class="dot"></span>Bright Cedar Lending</div>
  <div class="tag">Lowest Rates In Hawaii !!!!!</div>
  <div class="glow" role="img" aria-label="Faint sun and palm background decoration"></div>
</div>
<div class="label" style="left:820px;top:426px;width:368px">Envelope Option 1</div>

</body>
</html>
```